Business card design needed

We are a independent software development company specialising in financial and business custom applications and Quillmark Suite automation and integration.
Colours: Blue/Purple/Yellow/White
Target Market(s)
CFO's, CIO's, Financial Managers, Business Managers
Industry/Entity Type
Financial
Contact Information for Business Card
Dennis R Holbek
MV Systems (QLD) Pty Ltd
ABN: 53 904 218 617
PO Box 715
Harlow Point Qld 4619
Mobile: 0417 936 504
Email: programmer@mv-systems.example
Web: www.mv-systems.example
Netwave logo, Chatterly logo
Logo styles of interest
Abstract Logo
Requirements
Must have
- Flat screen computer monitor keyboard and mouse
Nice to have
- would like to see some binary digits ie. 1's and 0's incorporated in the background.

```html
<!DOCTYPE html>
<html lang="en">
<head>
<meta charset="utf-8">
<title>MV Systems business card</title>
<link href="https://fonts.googleapis.com/css2?family=Arimo:wght@400;700&display=swap" rel="stylesheet">
<style>
  :root {
    --page: #ffffff;
    --navy-top: #0c4475;
    --navy-bottom: #0757a0;
    --ink-blue: #0d63b0;
    --text-blue: #1a6ab8;
    --edge-blue: #2aa6e0;
    --panel-light: #ffffff;
    --panel-grey: #c2c4c7;
    --tab-grey: #e4e6e9;
    --white: #ffffff;
  }
  html, body {
    margin: 0;
    width: 1200px;
    height: 1082px;
    overflow: hidden;
    background: var(--page);
    font-family: "Arimo", Arial, sans-serif;
  }
  .card {
    position: absolute;
    left: 99px;
    top: 257px;
    width: 978px;
    height: 529px;
    overflow: hidden;
    background: linear-gradient(180deg, var(--navy-top), var(--navy-bottom));
  }
  .binary-backdrop {
    position: absolute;
    inset: 0;
    background:
      linear-gradient(90deg, rgba(255,255,255,0) 0%, rgba(255,255,255,0.05) 35%, rgba(255,255,255,0) 45%, rgba(255,255,255,0.06) 72%, rgba(255,255,255,0) 90%);
  }
  .name-tab {
    position: absolute;
    left: 596px;
    top: 60px;
    width: 382px;
    height: 67px;
    background: var(--tab-grey);
    border-radius: 20px 0 0 20px;
  }
  .name {
    position: absolute;
    left: 48px;
    top: 11px;
    margin: 0;
    font-weight: 700;
    font-size: 40px;
    line-height: 46px;
    color: var(--ink-blue);
    white-space: nowrap;
  }
  .details-panel {
    position: absolute;
    left: 0;
    top: 0;
  }
  .details {
    position: absolute;
    left: 83px;
    top: 274px;
    color: var(--text-blue);
  }
  .company {
    margin: 0 0 14px;
    font-weight: 700;
    font-size: 32px;
    line-height: 40px;
    color: var(--ink-blue);
    white-space: nowrap;
  }
  .contact {
    margin: 0;
    padding-left: 4px;
    font-size: 24px;
    line-height: 33px;
    white-space: nowrap;
  }
  .contact .label {
    display: inline-block;
    width: 59px;
  }
  .social {
    position: absolute;
    right: 37px;
    top: 462px;
    display: flex;
    gap: 16px;
    align-items: center;
  }
  .social-item {
    display: flex;
    align-items: center;
    gap: 6px;
    font-size: 15px;
    font-weight: 700;
    color: var(--white);
  }
  .social-item .mark {
    width: 14px;
    height: 14px;
    background: var(--edge-blue);
  }
</style>
</head>
<body>
  <div class="card">
    <div class="binary-backdrop" role="img" aria-label="Columns of faint binary digits across the blue background"></div>

    <div class="name-tab">
      <h1 class="name">Dennis R Holbek</h1>
    </div>

    <svg class="details-panel" width="978" height="529" viewBox="0 0 978 529">
      <defs>
        <linearGradient id="panelFill" x1="0" y1="0" x2="1" y2="0">
          <stop offset="0" stop-color="var(--panel-light)"/>
          <stop offset="1" stop-color="var(--panel-grey)"/>
        </linearGradient>
      </defs>
      <path d="M60 190 Q62 198 78 200 L638 256 Q662 262 660 282 L625 535 L-5 535 Z"
            fill="url(#panelFill)" stroke="var(--edge-blue)" stroke-width="7" stroke-linejoin="round"/>
    </svg>

    <div class="details">
      <h2 class="company">MV Systems (QLD) Pty Ltd</h2>
      <p class="contact">PO Box 715</p>
      <p class="contact">Harlow Point Qld 4619</p>
      <p class="contact"><span class="label">M:</span>0417 936 504</p>
      <p class="contact"><span class="label">E:</span>programmer@mv-systems.example</p>
      <p class="contact"><span class="label">W:</span>www.mv-systems.example</p>
    </div>

    <div class="social">
      <span class="social-item"><span class="mark"></span>Chatterly</span>
      <span class="social-item"><span class="mark"></span>Netwave</span>
    </div>
  </div>
</body>
</html>
```